Business Cards Needed For Veterinary Business

Looking for a business card design for a veterinary blood bank. We would like it to be clean and professional on appearance but still warm and inviting. We would like to utilize our logo and similar coloring. We will use our phone number, email, website, employee name, employee title.

We do not want a bunch of animated animal photos but do not need the style to be as clinical as a laboratory or human medical procedure office.

We are looking for some creative ideas to choose from so that we can generate a standout professional business card for our management team to utilize.

Target Market(s)

professionals

Industry/Entity Type

veterinary

Contact Information for Business Card

employee name, employee title, phone number, website URL, email

Font styles to use
Sans Serif

Colors
0054AA
0677BA
7BADD7
CADEEF
E8F1F8
EB3D1F
EC4F4E
F09395
F8D3D4
FCEDEE

Requirements
Nice to have
• creative design
Should not have
• animated photos

```html
<!DOCTYPE html>
<html lang="en">
<head>
<meta charset="utf-8">
<title>Kindred Veterinary Blood Bank – Business Cards</title>
<link rel="stylesheet" href="https://fonts.googleapis.com/css2?family=Open+Sans:wght@400;700&display=swap">
<style>
  :root {
    --backdrop: #2e2e2e;
    --card-white: #ffffff;
    --card-dark: #161616;
    --brand-red: #eb2227;
    --brand-blue: #0c4c9c;
    --text-light: #f2f2f2;
  }
  * { box-sizing: border-box; margin: 0; padding: 0; }
  html, body { width: 1200px; height: 780px; overflow: hidden; }
  body {
    background: var(--backdrop);
    font-family: "Open Sans", Arial, sans-serif;
    display: flex;
    align-items: center;
    justify-content: center;
    gap: 40px;
  }
  .card {
    position: relative;
    width: 540px;
    height: 310px;
    border-radius: 22px;
    overflow: hidden;
    background: var(--card-white);
  }
  .card-back .wave { position: absolute; inset: 0; width: 100%; height: 100%; }
  .brand {
    position: absolute;
    display: flex;
    align-items: center;
    gap: 12px;
  }
  .brand-dot {
    flex: none;
    border-radius: 50%;
    background: var(--brand-red);
  }
  .brand-name {
    color: var(--brand-red);
    font-weight: 700;
    text-transform: uppercase;
    line-height: 1.1;
  }
  .card-back .brand { left: 40px; top: 24px; }
  .card-back .brand-dot { width: 34px; height: 34px; }
  .card-back .brand-name { font-size: 19px; width: 220px; }
  .card-front .brand { left: 50%; top: 50%; transform: translate(-50%, -50%); gap: 18px; }
  .card-front .brand-dot { width: 64px; height: 64px; }
  .card-front .brand-name { font-size: 32px; width: 300px; }
  .contact {
    position: absolute;
    right: 30px;
    bottom: 16px;
    text-align: right;
    color: var(--text-light);
    font-size: 12px;
    line-height: 1.4;
  }
  .contact-name { color: var(--brand-red); font-weight: 700; font-size: 18px; text-transform: uppercase; letter-spacing: .5px; }
  .contact-title { margin-bottom: 5px; }
  .contact-address { margin-bottom: 5px; }
  .contact-line { display: flex; align-items: center; justify-content: flex-end; gap: 8px; }
  .contact-line svg { width: 12px; height: 12px; fill: var(--brand-red); }
</style>
</head>
<body>
  <section class="card card-back" aria-label="Business card, contact side">
    <svg class="wave" viewBox="0 0 540 310" preserveAspectRatio="none" aria-hidden="true">
      <path d="M0,60 C20,120 70,135 180,140 S420,122 540,138 L540,310 L0,310 Z" fill="var(--card-dark)"/>
      <path d="M0,60 C20,120 70,135 180,140 S420,122 540,138" fill="none" stroke="var(--brand-blue)" stroke-width="6"/>
      <path d="M0,30 C6,90 40,118 90,132 C40,112 18,85 14,30 Z" fill="var(--brand-red)"/>
    </svg>
    <div class="brand">
      <span class="brand-dot"></span>
      <span class="brand-name">Kindred Veterinary Blood Bank</span>
    </div>
    <div class="contact">
      <p class="contact-name">Daniel Reyes</p>
      <p class="contact-title">Managing Director</p>
      <p class="contact-address">18 Elm Row, Fairview<br>Ohio, Zip 45012</p>
      <p class="contact-line">555 014 2290
        <svg viewBox="0 0 24 24" aria-label="phone"><path d="M6.6 10.8a15.1 15.1 0 0 0 6.6 6.6l2.2-2.2a1 1 0 0 1 1-.25 11.4 11.4 0 0 0 3.6.57 1 1 0 0 1 1 1V20a1 1 0 0 1-1 1A17 17 0 0 1 3 4a1 1 0 0 1 1-1h3.5a1 1 0 0 1 1 1c0 1.25.2 2.45.57 3.57a1 1 0 0 1-.25 1z"/></svg>
      </p>
      <p class="contact-line">hello@kindredvbb.com
        <svg viewBox="0 0 24 24" aria-label="email"><path d="M2 5h20v14H2z M4 7v.4l8 5 8-5V7l-8 5z" fill-rule="evenodd"/></svg>
      </p>
      <p class="contact-line">www.kindredvbb.com
        <svg viewBox="0 0 24 24" aria-label="website"><circle cx="12" cy="12" r="10"/></svg>
      </p>
    </div>
  </section>

  <section class="card card-front" aria-label="Business card, brand side">
    <div class="brand">
      <span class="brand-dot"></span>
      <span class="brand-name">Kindred Veterinary Blood Bank</span>
    </div>
  </section>
</body>
</html>
```